Youth deer hunt give away flyer.

We need a flyer designed for a youth deer hunt giveaway that we are doing. We are an Illinois whitetail deer hunting outfitter. We house and feed our clients as well as providing them with a guided deer hunt. It needs to include images as well as details about the giveaway. Im looking for a proffesional, looking flyer

Target Market(s)

rednecks, hunters

Industry/Entity Type

Hunting

Font styles to use
Serif
Sans Serif

Colors
000000
dbdbdb
ffffff
474747

Requirements
Must have
• not sure
Nice to have
• not sure
Should not have
• not sure

```html
<!DOCTYPE html>
<html lang="en">
<head>
<meta charset="utf-8">
<title>2018 Youth Firearm Hunt – Harlan Ridge Outfitting</title>
<link rel="stylesheet" href="https://fonts.googleapis.com/css2?family=Ultra&family=Oswald:wght@600&family=Poppins:wght@400;500&family=Libre+Baskerville:wght@700&display=swap">
<style>
  :root {
    --black: #000000;
    --charcoal: #2b2b2b;
    --slate: #474747;
    --mist: #dbdbdb;
    --white: #ffffff;
    --body: #333333;
    --accent-red: #d9432f;
  }
  * { box-sizing: border-box; margin: 0; padding: 0; }
  html, body {
    width: 1040px; height: 1200px; overflow: hidden;
    background: var(--mist);
  }
  .flyer {
    position: relative;
    width: 928px; height: 1200px;
    margin: 0 auto;
    background: var(--white);
    overflow: hidden;
    font-family: "Poppins", sans-serif;
  }
  .hero {
    position: absolute; left: 0; top: 0; width: 928px; height: 663px;
    background:
      linear-gradient(180deg, rgba(0,0,0,0.35) 0%, rgba(0,0,0,0.05) 40%, rgba(0,0,0,0) 60%),
      linear-gradient(180deg, #2f3d2a 0%, #41522f 30%, #6f8a3e 52%, #7f9b47 70%, #6c8a3b 100%);
  }
  .hero-herd {
    position: absolute; left: 120px; top: 250px; width: 808px; height: 300px;
    background: radial-gradient(ellipse at 55% 50%, rgba(110,82,60,0.85) 0%, rgba(110,82,60,0.5) 45%, rgba(110,82,60,0) 75%);
  }
  .title {
    position: absolute; left: 0; right: 0; top: 48px;
    text-align: center;
    font-family: "Ultra", serif;
    color: var(--white);
    font-size: 58px; line-height: 76px; letter-spacing: 3px;
    text-shadow: 0 2px 4px rgba(0,0,0,0.5);
  }
  .dates {
    position: absolute; left: 0; right: 0; top: 208px;
    text-align: center;
    font-family: "Oswald", sans-serif; font-weight: 600;
    color: var(--white); font-size: 42px; letter-spacing: 1px;
    text-shadow: 0 2px 4px rgba(0,0,0,0.5);
  }
  .gallery {
    position: absolute; left: 0; top: 512px; width: 466px; height: 151px;
    background: var(--white);
  }
  .gallery-photo { position: absolute; top: 5px; height: 141px; }
  .gallery-photo.interior {
    left: 0; width: 226px;
    background: linear-gradient(135deg, #8a4a22 0%, #b76a33 45%, #5a2f17 100%);
  }
  .gallery-photo.cabin {
    left: 232px; width: 228px;
    background: linear-gradient(180deg, #e6e8e4 0%, #e6e8e4 40%, #c98a2e 41%, #b9762a 68%, #5f8a3a 69%, #4d7a30 100%);
  }
  .info-bar {
    position: absolute; right: 0; height: 46px;
    background: var(--charcoal);
    display: flex; align-items: center; justify-content: flex-end;
    padding-right: 42px;
    color: var(--white); font-size: 17px; letter-spacing: 1px;
  }
  .info-bar.follow {
    top: 486px; width: 325px; height: 44px;
    clip-path: polygon(22px 0, 100% 0, 100% 100%, 0 100%);
    font-family: "Libre Baskerville", serif; font-size: 15px;
    color: var(--accent-red); gap: 14px;
  }
  .social-dot { width: 18px; height: 18px; border-radius: 3px; background: var(--white); }
  .info-bar.call {
    top: 547px; width: 362px;
    clip-path: polygon(22px 0, 100% 0, 100% 100%, 0 100%);
  }
  .info-bar.web {
    top: 603px; width: 400px; height: 48px;
    clip-path: polygon(22px 0, 100% 0, 100% 100%, 0 100%);
  }
  .perks {
    position: absolute; left: 0; top: 663px; width: 928px; height: 139px;
    background: var(--charcoal);
    list-style: none;
    padding: 14px 0 0 38px;
    color: var(--white); font-size: 18.5px; letter-spacing: 0.6px; line-height: 28.5px;
  }
  .perks li { display: flex; align-items: center; gap: 14px; }
  .perks svg { flex: none; }
  .section-heading {
    position: absolute; left: 40px;
    display: flex; align-items: center; gap: 12px;
    font-family: "Oswald", sans-serif; font-weight: 600;
    font-size: 20px; letter-spacing: 1px; color: var(--charcoal);
  }
  .section-heading::before {
    content: ""; width: 16px; height: 16px;
    background: linear-gradient(135deg, var(--slate) 50%, var(--black) 50%);
  }
  .about-heading { top: 825px; }
  .contact-heading { top: 1045px; }
  .about-copy {
    position: absolute; left: 40px; top: 870px; width: 850px;
    font-size: 14.2px; line-height: 22.6px; color: var(--body); letter-spacing: 0.3px;
  }
  .about-copy p + p { margin-top: 4px; }
  .contact-details {
    position: absolute; left: 39px; top: 1093px;
    font-size: 17.5px; line-height: 23px; color: var(--black); letter-spacing: 0.5px;
  }
  .contact-name {
    font-family: "Libre Baskerville", serif; font-weight: 700; font-size: 15px;
    color: var(--charcoal);
  }
  .brand-mark {
    position: absolute; left: 660px; top: 1050px; width: 230px;
    display: flex; flex-direction: column; align-items: center; gap: 16px;
  }
  .brand-circle { width: 70px; height: 70px; border-radius: 50%; background: var(--black); }
  .brand-name {
    font-family: "Libre Baskerville", serif; font-weight: 700;
    font-size: 21px; letter-spacing: 1px; color: var(--black); text-align: center;
  }
</style>
</head>
<body>
  <main class="flyer">
    <div class="hero" role="img" aria-label="Photo of a herd of antlered deer grazing on a green meadow with large trees behind">
      <div class="hero-herd"></div>
    </div>
    <h1 class="title">2018 YOUTH<br>FIREARM HUNT</h1>
    <p class="dates">OCTOBER 6-8, 2018</p>

    <div class="gallery">
      <div class="gallery-photo interior" role="img" aria-label="Photo of the wood-panelled cabin interior with kitchen bar and seating"></div>
      <div class="gallery-photo cabin" role="img" aria-label="Photo of the log cabin exterior with green roof on a lawn"></div>
    </div>

    <div class="info-bar follow">FOLLOW US ON <span class="social-dot"></span></div>
    <div class="info-bar call">CALL TODAY:(217)555-0148</div>
    <div class="info-bar web">www.harlanridgehunts.com</div>

    <ul class="perks">
      <li><svg width="12" height="12" viewBox="0 0 12 12"><g fill="#fff"><rect width="5" height="5"/><rect x="7" width="5" height="5"/><rect y="7" width="5" height="5"/><rect x="7" y="7" width="5" height="5"/></g></svg>4 night stay in our private cabin that include meals for 2 parents and the child.</li>
      <li><svg width="12" height="12" viewBox="0 0 12 12"><g fill="#fff"><rect width="5" height="5"/><rect x="7" width="5" height="5"/><rect y="7" width="5" height="5"/><rect x="7" y="7" width="5" height="5"/></g></svg>Guided shotgun hunt on strictly managed properties.</li>
      <li><svg width="12" height="12" viewBox="0 0 12 12"><g fill="#fff"><rect width="5" height="5"/><rect x="7" width="5" height="5"/><rect y="7" width="5" height="5"/><rect x="7" y="7" width="5" height="5"/></g></svg>Ground blinds in place.</li>
      <li><svg width="12" height="12" viewBox="0 0 12 12"><g fill="#fff"><rect width="5" height="5"/><rect x="7" width="5" height="5"/><rect y="7" width="5" height="5"/><rect x="7" y="7" width="5" height="5"/></g></svg>Permit and license fees are the hunters responsibility.</li>
    </ul>

    <h2 class="section-heading about-heading">ABOUT US</h2>
    <div class="about-copy">
      <p>Harlan Ridge Outfitting is a family owned and operated deer hunting outfitter located in Morgan and Scott Counties in west central Illinois. We provide low pressure, trophy whitetail hunts on privately owned farms across the region. The Harlans are lifelong residents and hunters of Morgan County, with the family farm being established well over 150 years ago.</p>
      <p>To go along with guiding deer and turkey hunters, we also offer a wide variety of professional hunting services that include whitetail land consulting, scouting services,<br>CRP and food plot plantings and more.</p>
    </div>

    <h2 class="section-heading contact-heading">CONTACT</h2>
    <div class="contact-details">
      <p class="contact-name">WADE HARLAN:</p>
      <p>1847 Ridge Road Millbrook, Illinois 62999</p>
      <p>hello@harlanridgehunts.com</p>
    </div>

    <div class="brand-mark">
      <span class="brand-circle"></span>
      <span class="brand-name">HARLAN RIDGE</span>
    </div>
  </main>
</body>
</html>
```